Redesign This Psychology Website

We would like a slight redesign of this successful psychology (relationship counselling) website:

www.TheWillowNook.com.au

We are updating the website, and we'd like a slight refresh of the design and style.

Please keep to very similar colours, and use the same logo. We're looking for around 10 page templates, however the main one is the home page.

Keep in mind, this website already converts quite well, so we want a new, fresh design in keeping with this one. Please don't bother designing something too extremely different.

thanks :)

Target Market(s)

couples who are looking for relationship counselling. Men and women, 25 - 70, across Australia

Industry/Entity Type

Psychology

Number of Pages Required

5+ page

Font styles to use
Sans Serif

Colors
87cfc6
b7a5cd
ec1f27
ffffff
cee9f5

Requirements
Must have
• a similar look to the current design, just looking for a slight refresh.
• Search bar
• Areas for lots of photos
• same logo
• lots of content areas
Nice to have
• great content areas, where we can display a lot of content and our areas.
Should not have
• no colors like orange, etc.
• should not have a totally different feel.

```html
<!DOCTYPE html>
<html lang="en">
<head>
<meta charset="utf-8">
<title>The Willow Nook – Relationship Counselling</title>
<link href="https://fonts.googleapis.com/css2?family=Open+Sans:wght@300;400;600;700;800&display=swap" rel="stylesheet">
<style>
:root{
  --teal:#87cfc6;
  --teal-dark:#5fb8ae;
  --lilac:#b7a5cd;
  --lilac-icon:#a08cc4;
  --red:#ec1f27;
  --white:#ffffff;
  --sky:#cee9f5;
  --topbar:#6b6461;
  --ink:#333333;
  --muted:#777777;
  --soft:#f3f3f3;
  --line:#e2e2e2;
}
*{margin:0;padding:0;box-sizing:border-box}
html,body{width:1200px;height:2659px;overflow:hidden}
body{font-family:"Open Sans",Arial,sans-serif;color:var(--ink);background:var(--white);position:relative}
a{color:inherit;text-decoration:none}
.abs{position:absolute}

/* top bar */
.topbar{position:absolute;left:0;top:0;width:1200px;height:30px;background:var(--topbar);color:#fff;font-size:10.5px;font-weight:600;letter-spacing:.3px}
.topbar .left{position:absolute;left:131px;top:8px}
.topbar .right{position:absolute;right:131px;top:8px}
.topbar span.sep{margin:0 6px;opacity:.7}

/* header */
.header{position:absolute;left:0;top:30px;width:1200px;height:114px;background:#fff}
.brand{position:absolute;left:131px;top:22px;display:flex;align-items:center;gap:12px}
.brand-dot{width:56px;height:56px;border-radius:50%;background:var(--teal-dark)}
.brand-name{font-size:33px;font-weight:400;color:var(--teal-dark);line-height:1}
.brand-tag{position:absolute;left:131px;top:80px;font-size:14px;color:var(--teal-dark);font-weight:600}
.search{position:absolute;left:514px;top:41px;width:310px;height:36px;border:1px solid var(--line);background:#fff}
.search .ph{position:absolute;left:14px;top:10px;font-size:11px;color:#aaa;font-style:italic}
.search .btn{position:absolute;right:4px;top:5px;width:66px;height:24px;background:var(--teal);color:#fff;font-size:10px;font-weight:700;text-align:center;line-height:24px}
.callus{position:absolute;left:851px;top:46px;font-size:14px;color:#666;display:flex;align-items:center;gap:10px}
.callus b{color:var(--red);font-size:19px;font-weight:400}

/* nav */
.nav{position:absolute;left:0;top:144px;width:1200px;height:49px;background:var(--teal);color:#fff;font-size:11.5px;font-weight:700;letter-spacing:.4px}
.nav span{position:absolute;top:17px}

/* hero */
.hero{position:absolute;left:0;top:193px;width:1200px;height:566px;background:linear-gradient(100deg,#d9d2c8 0%,#c9b49c 30%,#8aa3c0 55%,#d6cfc6 80%,#b9a89a 100%)}
.hero-title{position:absolute;right:131px;top:418px;font-size:44px;color:#fff;font-weight:300;letter-spacing:.5px}
.hero-title b{font-weight:800}
.hero-sub{position:absolute;right:131px;top:480px;width:740px;text-align:right;font-size:14px;line-height:26px;color:#fff}
.hero-btn{position:absolute;left:918px;top:553px;width:149px;height:37px;background:var(--red);color:#fff;font-size:12px;font-weight:700;text-align:center;line-height:37px}
.arrow-circ{position:absolute;top:418px;width:28px;height:28px;border-radius:50%;background:#fff}

/* service strip */
.services{position:absolute;left:0;top:759px;width:1200px;height:246px;background:var(--soft)}
.svc{position:absolute;top:675px;width:230px;text-align:center}
.svc .pic{width:160px;height:160px;border-radius:50%;border:6px solid #fff;margin:0 auto;box-shadow:0 0 0 1px #ddd}
.svc h3{font-size:13px;font-weight:400;color:#444;margin-top:22px;letter-spacing:.2px}
.svc .need{font-size:12px;color:var(--teal-dark);margin-top:3px}
.svc p{font-size:10.5px;color:#666;line-height:19px;margin-top:4px;padding:0 14px}
.svc .more{font-size:11px;color:var(--red);margin-top:6px}
.svc-div{position:absolute;top:860px;width:1px;height:105px;background:var(--line)}

/* find band */
.find{position:absolute;left:0;top:1005px;width:1200px;height:106px;background:var(--teal);color:#fff}
.find h4{position:absolute;left:131px;top:31px;font-size:17px;font-weight:400;line-height:26px}
.find label{position:absolute;top:28px;font-size:10.5px}
.find .field{position:absolute;top:48px;width:208px;height:30px;background:#fff}
.find .go{position:absolute;left:1003px;top:48px;width:64px;height:30px;background:var(--red);font-size:11px;font-weight:700;text-align:center;line-height:30px}

/* about */
.about-kicker{position:absolute;left:131px;top:1180px;font-size:17px;color:#333}
.about-title{position:absolute;left:131px;top:1211px;font-size:25px;font-weight:700;color:#333;letter-spacing:.5px}
.about-text{position:absolute;left:131px;top:1262px;width:410px;font-size:11px;line-height:24px;color:#555}
.about-text p+p{margin-top:16px}
.about-btn{position:absolute;left:131px;top:1420px;width:101px;height:32px;background:var(--red);color:#fff;font-size:11px;font-weight:700;text-align:center;line-height:32px}
.video{position:absolute;left:606px;top:1175px;width:461px;height:291px;background:linear-gradient(90deg,#8fb8cf 0%,#c7cfd4 45%,#e0b98e 75%,#c99a6a 100%)}
.video .play{position:absolute;left:191px;top:107px;width:78px;height:78px;border-radius:50%;background:rgba(60,60,60,.75)}
.video .cap{position:absolute;left:0;top:226px;width:230px;height:34px;background:rgba(255,255,255,.85);font-size:18px;color:#333;padding:7px 12px;letter-spacing:1px}

/* gallery */
.gallery{position:absolute;left:0;top:1528px;width:1200px;height:393px;background:var(--sky)}
.gallery h2{position:absolute;left:0;top:56px;width:1200px;text-align:center;font-size:25px;font-weight:700;color:#333}
.g-item{position:absolute;top:119px;width:300px}
.g-item .ph{height:191px}
.g-item span{display:block;text-align:center;font-size:11px;font-weight:700;margin-top:12px;color:#333}

/* topics */
.topic{position:absolute;width:290px}
.topic .ico{position:absolute;left:0;top:0;width:67px;height:67px;border-radius:50%;border:1.5px solid var(--lilac);display:flex;align-items:center;justify-content:center}
.topic h5{position:absolute;left:90px;top:2px;width:200px;font-size:14px;font-weight:400;color:#333;line-height:21px}
.topic p{position:absolute;left:90px;top:50px;width:200px;font-size:10.5px;color:#777;line-height:19px}

/* blog */
.blog{position:absolute;left:0;top:2255px;width:1200px;height:294px;background:var(--teal);color:#fff}
.blog h2{position:absolute;left:0;top:50px;width:1200px;text-align:center;font-size:25px;font-weight:700}
.blog .post-img{position:absolute;top:120px;width:138px;height:112px}
.blog .post-title{position:absolute;top:133px;width:260px;font-size:13px;line-height:23px}
.blog .post-date{position:absolute;top:185px;font-size:13px;font-weight:700}
.blog .nav-dot{position:absolute;top:58px;width:15px;height:15px;border-radius:50%;border:1.5px solid #fff}

/* footer */
.footer{position:absolute;left:0;top:2549px;width:1200px;height:110px;background:#fff}
.footer .mark{position:absolute;left:131px;top:35px;width:46px;height:46px;border-radius:50%;background:var(--teal-dark)}
.footer .copy{position:absolute;left:199px;top:36px;font-size:11px;color:#555}
.footer .links{position:absolute;left:199px;top:62px;font-size:11px;color:#555}
.footer .follow{position:absolute;left:918px;top:49px;font-size:11px;color:#555}
.footer .soc{position:absolute;top:43px;width:24px;height:24px;border-radius:50%}
</style>
</head>
<body>

<div class="topbar">
  <div class="left">HOME<span class="sep">|</span>ABOUT<span class="sep">|</span>RESOURCES<span class="sep">|</span>BLOG<span class="sep">|</span>SHOP<span class="sep">|</span>CART</div>
  <div class="right">JOIN OUR ASSOCIATE PROGRAM<span class="sep">|</span>MARRIAGE COUNSELLING<span class="sep">|</span>RELATIONSHIP COUNSELLING</div>
</div>

<header class="header">
  <div class="brand"><div class="brand-dot"></div><div class="brand-name">The Willow Nook</div></div>
  <div class="brand-tag">helping you create loving relationships</div>
  <div class="search"><span class="ph">Information Topic</span><span class="btn">SEARCH</span></div>
  <div class="callus">
    <svg width="16" height="16" viewBox="0 0 24 24"><path fill="#ec1f27" d="M6.6 10.8c1.4 2.8 3.8 5.1 6.6 6.6l2.2-2.2c.3-.3.7-.4 1-.2 1.1.4 2.3.6 3.6.6.6 0 1 .4 1 1V20c0 .6-.4 1-1 1C10.6 21 3 13.4 3 4c0-.6.4-1 1-1h3.5c.6 0 1 .4 1 1 0 1.3.2 2.5.6 3.6.1.3 0 .7-.2 1L6.6 10.8z"/></svg>
    CALL US ON : <b>1300 555 018</b>
  </div>
</header>

<nav class="nav">
  <span style="left:145px">COUNSELLING TYPES ▾</span>
  <span style="left:316px">RELATIONSHIP COUNSELLING LOCATIONS</span>
  <span style="left:608px">SEX THERAPY LOCATIONS</span>
  <span style="left:805px">QUIZZES</span>
  <span style="left:907px">F.A.Q.'S</span>
  <span style="left:1000px">CONTACT</span>
</nav>

<section class="hero" role="img" aria-label="Photo of a smiling couple embracing on a sofa"></section>
<div class="arrow-circ" style="left:64px"></div>
<svg class="abs" style="left:64px;top:418px" width="28" height="28" viewBox="0 0 28 28"><path d="M16 8l-6 6 6 6" fill="none" stroke="#555" stroke-width="3"/></svg>
<div class="arrow-circ" style="left:1107px"></div>
<svg class="abs" style="left:1107px;top:418px" width="28" height="28" viewBox="0 0 28 28"><path d="M12 8l6 6-6 6" fill="none" stroke="#555" stroke-width="3"/></svg>
<div class="hero-title">RELATIONSHIP <b>COUNSELLING</b></div>
<div class="hero-sub">We can also assist you if you want individual help and guidance on your relationship, so you can learn what the patterns in your relationships are showing you about yourself.</div>
<a class="hero-btn">GET STARTED TODAY</a>

<section class="services"></section>
<div class="svc" style="left:107px"><div class="pic" role="img" aria-label="Photo of a couple talking" style="background:linear-gradient(135deg,#c8c2ba,#b84b4b)"></div><h3>RELATIONSHIP COUNSELLING</h3><div class="need">Do you need help with:</div><p>Communication, Recovering from an affair, Loss of intimacy &amp; love...</p><div class="more">Learn More ➞</div></div>
<div class="svc-div" style="left:341px"></div>
<div class="svc" style="left:353px"><div class="pic" role="img" aria-label="Photo of a couple resting together" style="background:linear-gradient(135deg,#1e3a2a,#d8d2c6)"></div><h3>SEX THERAPY COUNSELLING</h3><div class="need">Do you need help with:</div><p>Low libido , Erectile difficulties, Premature ejaculation, Differing...</p><div class="more">Learn More ➞</div></div>
<div class="svc-div" style="left:587px"></div>
<div class="svc" style="left:603px"><div class="pic" role="img" aria-label="Photo of a couple in a tense moment" style="background:linear-gradient(135deg,#d8cfc4,#c79a7a)"></div><h3>ANGER MANAGEMENT COUNSELLING</h3><div class="need">Do you need help with:</div><p>Managing angry outbursts, expressing your anger in healthy ways...</p><div class="more">Learn More ➞</div></div>
<div class="svc-div" style="left:856px"></div>
<div class="svc" style="left:851px"><div class="pic" role="img" aria-label="Photo of a smiling woman" style="background:linear-gradient(135deg,#6c5a52,#d9cbc0)"></div><h3>NARCISSISM COUNSELLING</h3><div class="need">Do you need help with:</div><p>Managing narcissistic, superior, entitled, arrogant and lack of empathy...</p><div class="more">Learn More ➞</div></div>

<section class="find">
  <h4>Find Our Psychologist<br>Near You</h4>
  <label style="left:339px">Type Of Counselling :</label><div class="field" style="left:339px"></div>
  <label style="left:556px">Location (or)</label><div class="field" style="left:556px"></div>
  <label style="left:772px">Postcode :</label><div class="field" style="left:772px"></div>
  <a class="go">SEARCH</a>
</section>

<div class="about-kicker">WE SPECIALISE IN RELATIONSHIP</div>
<h2 class="about-title">&amp; MARRIAGE COUNSELLING</h2>
<div class="about-text">
  <p>At the Willow Nook, we are a group of PSYCHOLOGISTS, Australia wide who are passionate about relationships and helping you with yours.</p>
  <p>Our vision is to provide the most highly regarded and comprehensive marriage counselling and relationship counselling, and sex therapy in Australia, at reasonable and affordable rates.</p>
</div>
<a class="about-btn">LEARN MORE</a>
<div class="video" role="img" aria-label="Video still of the practice director speaking">
  <div class="play"></div>
  <svg class="abs" style="left:191px;top:107px" width="78" height="78" viewBox="0 0 78 78"><path d="M31 24l25 15-25 15z" fill="#fff"/></svg>
  <div class="cap">DANA MORROW</div>
</div>

<section class="gallery">
  <svg class="abs" style="left:405px;top:63px" width="12" height="14" viewBox="0 0 12 14"><path d="M9 1L3 7l6 6" fill="none" stroke="#888" stroke-width="2.5"/></svg>
  <h2>PHOTO GALLERY</h2>
  <svg class="abs" style="left:783px;top:63px" width="12" height="14" viewBox="0 0 12 14"><path d="M3 1l6 6-6 6" fill="none" stroke="#888" stroke-width="2.5"/></svg>
  <div class="g-item" style="left:0"><div class="ph" role="img" aria-label="Photo of a woman in a counselling session" style="background:linear-gradient(90deg,#8fae6a,#c9c4be)"></div><span>EXCEPTEUR SINT</span></div>
  <div class="g-item" style="left:300px"><div class="ph" role="img" aria-label="Photo of a couple on a couch" style="background:linear-gradient(90deg,#c4bdb6,#b85a5a,#8e95a6)"></div><span>EXCEPTEUR SINT</span></div>
  <div class="g-item" style="left:600px"><div class="ph" role="img" aria-label="Photo of a psychologist at a desk" style="background:linear-gradient(90deg,#dfe3e6,#aab4bc,#4a4f57)"></div><span>EXCEPTEUR SINT</span></div>
  <div class="g-item" style="left:900px"><div class="ph" role="img" aria-label="Photo of two women talking" style="background:linear-gradient(90deg,#b0774f,#d9d0c6,#6fa7c9)"></div><span>EXCEPTEUR SINT</span></div>
</section>

<div class="topic" style="left:131px;top:1975px"><div class="ico"><svg width="30" height="28" viewBox="0 0 24 22"><path fill="#a08cc4" d="M12 21L2.5 11.5A5.5 5.5 0 0 1 12 4a5.5 5.5 0 0 1 9.5 7.5z"/></svg></div><h5>How to deal with an affair?</h5><p>Natus error sit voluptatem accusantium doloremque omnis iste...</p></div>
<div class="topic" style="left:457px;top:1975px"><div class="ico"><svg width="32" height="32" viewBox="0 0 32 32" fill="none" stroke="#a08cc4" stroke-width="2.5"><circle cx="14" cy="16" r="6"/><path d="M18.5 11.5L25 5M20 5h5v5M14 22v7M10.5 26h7"/></svg></div><h5>Same Sex Relationships &amp; Counselling</h5><p>Natus error sit voluptatem accusantium doloremque omnis iste...</p></div>
<div class="topic" style="left:785px;top:1975px"><div class="ico"><svg width="34" height="26" viewBox="0 0 34 26" fill="#a08cc4"><circle cx="8" cy="7" r="4"/><circle cx="26" cy="7" r="4"/><circle cx="17" cy="6" r="5"/><path d="M1 22c0-5 3-8 7-8s5 2 5 2H1zM33 22c0-5-3-8-7-8s-5 2-5 2h12zM8 25c0-6 4-10 9-10s9 4 9 10z"/></svg></div><h5>Are you living with a narcissist</h5><p>Natus error sit voluptatem accusantium doloremque omnis iste...</p></div>
<div class="topic" style="left:131px;top:2115px"><div class="ico"><svg width="26" height="28" viewBox="0 0 26 28" fill="#a08cc4"><circle cx="13" cy="8" r="6"/><path d="M1 27c0-7 5-12 12-12s12 5 12 12z"/></svg></div><h5>Is one of you an Intimacy Withholder</h5><p>Natus error sit voluptatem accusantium doloremque omnis iste...</p></div>
<div class="topic" style="left:457px;top:2115px"><div class="ico"><svg width="34" height="22" viewBox="0 0 34 22"><path d="M1 11C6 3 28 3 33 11 28 19 6 19 1 11z" fill="#a08cc4"/><circle cx="17" cy="11" r="5" fill="#fff"/><circle cx="17" cy="11" r="2.5" fill="#a08cc4"/></svg></div><h5>Is too much porn affecting your relationship</h5><p>Natus error sit voluptatem accusantium doloremque omnis iste...</p></div>
<div class="topic" style="left:785px;top:2115px"><div class="ico"><svg width="32" height="32" viewBox="0 0 32 32" fill="none" stroke="#a08cc4"><circle cx="16" cy="16" r="11" stroke-width="6"/><circle cx="16" cy="16" r="14" stroke-width="1.5"/><circle cx="16" cy="16" r="5" stroke-width="1.5"/></svg></div><h5>Is your relationship safe? Is your partner controlling?</h5><p>Natus error sit voluptatem accusantium doloremque omnis iste...</p></div>

<section class="blog">
  <h2>RECENTBLOG</h2>
  <div class="nav-dot" style="left:1025px"></div>
  <div class="nav-dot" style="left:1044px"></div>
  <div class="post-img" style="left:131px" role="img" aria-label="Photo of a couple hugging" style="background:#c66"></div>
  <div class="post-img" style="left:131px;background:linear-gradient(135deg,#e9c6a8,#c2342e)" role="img" aria-label="Photo of a couple hugging"></div>
  <div class="post-title" style="left:295px">Do You Wonder Why You and Your Partner Are Together?</div>
  <div class="post-date" style="left:295px">OCTOBER 19, 2016</div>
  <div class="post-img" style="left:640px;background:linear-gradient(135deg,#d7d0c9,#7d9bb8)" role="img" aria-label="Photo of a couple sitting apart"></div>
  <div class="post-title" style="left:803px">Letter for a Partner Doubtful About Relationship Counselling</div>
  <div class="post-date" style="left:803px">FEBRUARY 3, 2017</div>
</section>

<footer class="footer">
  <div class="mark"></div>
  <div class="copy">Copyrights © thewillownook . 2017 | Allrights Reserved.</div>
  <div class="links">Privacy Policy | Terms &amp; Conditions | Site Map | Associate Psychologists Program | Contact Us</div>
  <div class="follow">Follow Us :</div>
  <div class="soc" style="left:978px;background:#3b5998"></div>
  <div class="soc" style="left:1010px;background:#29a9e1"></div>
  <div class="soc" style="left:1042px;background:#dc4a38"></div>
</footer>

</body>
</html>
```